Website Design for new skincare product launch/rebranding

The Dew Harbor website is currently live and built through Pagelume.com. While the existing site has served as a strong starting point, I’m now looking to elevate the overall experience with a complete redesign that reflects the growth and vision of the brand. This will be a full visual and functional revamp — not just a refresh — with the goal of creating a more elevated, intuitive, and conversion-focused platform. I’m looking for a designer who can not only reimagine the layout and visuals, but also collaborate on optimizing the user journey and site structure for both storytelling and sales.

Target Market(s)

Age 25- 45 (core), with secondary appeal to 18-55. Primarily women, but gender inclusive. Wellness/Holistic Beauty/Organic Ingredients, Botanical.

Industry/Entity Type

Beauty, aesthetics, wellness.

Number of Pages Required

5+ page

Font styles to use
Other font styles liked:
• Thorvale Sans Family

Colors

Designer to choose colors to be used in the design.

Requirements
Must have
• Include standard pages (Home, Our Story/Values, Shop, Product Detail with ingredients/description/etc., Contact) and any other recommended sections to optimize conversion. Minimal, clean, calming visual. Seamlessly integrate with Vendara for all product sales.
Nice to have
• Company colors are attached in images, along with first two products that are launching. One called Lumivelt, and one called Serapoise. Fonts and shapes need to align accordingly. Feel elevated, neutral, and luxe while maintaining a grounded, earthy minimalism. Visual inspiration includes brands like Maple Tenet, Vessa Orlaine, and TOrveli — minimal yet high-end, with thoughtful use of whitespace, typography, and subtle movement. Would LOVE to have movement (short clip GIF) on either the home page or ingredient page, reference TOrveli website (homepage or LumaKnit Process™ Tab)
Should not have
• dark colors, complex design elements, too many different fonts. For ingredients, stick to botanical images and information only, with no mentions of CBD or use of leaf imagery.

```html
<!DOCTYPE html>
<html lang="en">
<head>
<meta charset="utf-8">
<title>Dew Harbor — Skincare Aligned With You</title>
<link href="https://fonts.googleapis.com/css2?family=Playfair+Display:wght@400;500;700&family=Nunito+Sans:wght@300;400;600;700&display=swap" rel="stylesheet">
<style>
:root{
  --ink:#2b2623;
  --ink-soft:#4a4440;
  --muted:#8a8581;
  --topbar:#a8a49e;
  --white:#ffffff;
  --blush:#e3dbd8;
  --hero-peach:#ebc9a6;
  --card-bg:#f8f7f6;
  --formula:#d2ab8a;
  --tools:#93ab8a;
  --line:#3a3431;
}
*{margin:0;padding:0;box-sizing:border-box}
html,body{width:1200px;height:4428px;overflow:hidden}
body{position:relative;background:var(--white);color:var(--ink);font-family:"Nunito Sans",Arial,sans-serif}
.abs{position:absolute}

.topbar{left:0;top:0;width:1200px;height:31px;background:var(--topbar);font-size:12px;color:var(--ink);display:flex;align-items:center;justify-content:center}
.header{left:0;top:31px;width:1200px;height:107px;background:var(--white)}
.brand{left:100px;top:0;height:107px;display:flex;align-items:center;font-family:"Playfair Display",Georgia,serif;font-size:24px;letter-spacing:1px;color:#a9a4a0}
.nav{left:412px;top:44px;display:flex;gap:19px;font-size:14px;color:var(--muted)}
.nav .active{color:var(--ink)}
.icons{left:934px;top:41px;display:flex;gap:19px}
.icons svg{width:24px;height:24px;stroke:var(--ink);fill:none;stroke-width:1.6}

.hero{left:0;top:138px;width:1200px;height:512px;background:linear-gradient(90deg,#efd3b6 0%,var(--hero-peach) 45%,#e6bd97 100%)}
.hero-photo{left:540px;top:0;width:660px;height:512px;background:radial-gradient(ellipse at 62% 40%,#d79c74 0%,#e3b08a 40%,rgba(230,189,151,0) 75%)}
.hero-title{font-family:"Playfair Display",Georgia,serif;font-weight:700;font-size:92px;line-height:1;color:var(--ink);letter-spacing:1px}
.btn{border:1.5px solid var(--line);border-radius:4px;display:flex;align-items:center;justify-content:center;font-size:14px;letter-spacing:.5px;color:var(--ink)}

.bestseller{left:0;top:650px;width:1200px;height:1483px;background:var(--blush)}
.h2{font-family:"Playfair Display",Georgia,serif;font-size:44px;line-height:50px;font-weight:400;color:var(--ink);left:0;width:1200px;text-align:center}
.card{width:312px;height:404px;top:858px}
.card-model{background:linear-gradient(160deg,#6a5748 0%,#b89a86 45%,#d9cfc9 100%)}
.card-serum{background:linear-gradient(180deg,#f8f7f6 0%,#e9e8e6 100%)}
.card-balm{background:linear-gradient(180deg,#f8f7f6 0%,#ecebef 100%)}
.add-cart{left:0;bottom:0;width:100%;height:66px;background:rgba(140,135,130,.75);color:#fff;font-size:15px;display:flex;align-items:center;justify-content:center}
.pname{width:312px;top:1286px;font-size:15px;font-weight:700;text-align:center}
.pdesc{width:312px;top:1318px;font-size:12.5px;line-height:19px;color:var(--ink-soft);text-align:center;padding:0 28px}
.price{width:312px;top:1369px;font-size:13px;text-align:center;color:var(--ink-soft)}
.lead{left:0;width:1200px;text-align:center;font-size:29px;line-height:50px;font-weight:300;color:var(--ink)}

.tile{top:2133px;height:563px}
.tile-label{font-family:"Playfair Display",Georgia,serif;font-size:44px;line-height:50px;color:#fff;text-align:center;width:100%;left:0;top:390px}

.feature{top:2985px;width:300px;text-align:center}
.feature svg{width:80px;height:80px;stroke:var(--ink-soft);fill:none;stroke-width:1.6}
.feature span{display:block;margin-top:16px;font-size:25px;white-space:nowrap;color:var(--ink)}

.strip{top:3612px;height:285px}

.footer{left:0;top:3907px;width:1200px;height:521px;background:var(--blush)}
.flinks{font-size:14.5px;line-height:30px;color:var(--ink-soft);text-align:center;width:300px}
.fbrand{left:0;width:1200px;top:4050px;text-align:center;font-family:"Playfair Display",Georgia,serif;font-size:32px;letter-spacing:1px;color:#a9a4a0}
.signup{left:447px;width:304px;text-align:center}
.email{left:447px;top:4236px;width:304px;height:30px;border-bottom:1px solid #8a8581;display:flex;justify-content:space-between;align-items:center;font-size:12.5px;color:var(--ink-soft);padding:0 10px}
.copy{left:0;width:1200px;top:4376px;text-align:center;font-size:14px;color:var(--ink-soft)}
</style>
</head>
<body>

<div class="abs topbar">Enjoy free shipping on your first order</div>

<header class="abs header">
  <div class="abs brand">DEW HARBOR</div>
  <nav class="abs nav">
    <span class="active">Home</span><span>Our Story</span><span>Shop</span><span>Product Details</span><span>Contact</span>
  </nav>
  <div class="abs icons">
    <svg viewBox="0 0 24 24"><path d="M12 20s-8-5-8-11a4.5 4.5 0 0 1 8-2.5A4.5 4.5 0 0 1 20 9c0 6-8 11-8 11z"/></svg>
    <svg viewBox="0 0 24 24"><circle cx="11" cy="11" r="7"/><path d="M16 16l4 4"/></svg>
    <svg viewBox="0 0 24 24"><circle cx="12" cy="8" r="4"/><path d="M4 21c1-5 4-7 8-7s7 2 8 7"/></svg>
    <svg viewBox="0 0 24 24"><path d="M2 4h3l2.5 11h11l2-8H6.5"/><circle cx="9" cy="19.5" r="1.4"/><circle cx="17" cy="19.5" r="1.4"/></svg>
  </div>
</header>

<section class="abs hero">
  <div class="abs hero-photo" role="img" aria-label="Profile portrait of a woman with auburn hair in a bun, eyes closed, hand resting at her jaw"></div>
  <div class="abs hero-title" style="left:98px;top:80px">SKINCARE</div>
  <div class="abs hero-title" style="left:203px;top:183px">ALIGNED</div>
  <div class="abs hero-title" style="left:95px;top:286px">WITH YOU</div>
  <div class="abs btn" style="left:263px;top:403px;width:174px;height:47px">SHOP NOW</div>
</section>

<section class="abs bestseller"></section>
<h2 class="abs h2" style="top:733px">Our Bestseller</h2>

<div class="abs card card-model" style="left:100px" role="img" aria-label="Woman with curly hair applying serum with a dropper">
  <div class="abs add-cart">ADD TO CART</div>
</div>
<div class="abs card card-serum" style="left:445px" role="img" aria-label="Product photo of the Lumivelt serum bottle on a white background"></div>
<div class="abs card card-balm" style="left:789px" role="img" aria-label="Product photo of the Serapoise balm stick on a white background"></div>

<div class="abs pname" style="left:100px">Lumivelt</div>
<div class="abs pdesc" style="left:100px">A weightless, dew-enhancing serum for radiant skin.</div>
<div class="abs price" style="left:100px">$ 25.00</div>
<div class="abs pname" style="left:445px">Lumivelt</div>
<div class="abs pdesc" style="left:445px">A weightless, dew-enhancing serum for radiant skin.</div>
<div class="abs price" style="left:445px">$ 25.00</div>
<div class="abs pname" style="left:789px">Serapoise</div>
<div class="abs pdesc" style="left:789px">A barrier-strengthening hydrator for everyday resilience..</div>
<div class="abs price" style="left:789px">$ 25.00</div>

<h2 class="abs h2" style="top:1531px">A Mindful Approach to<br>Skin Health</h2>
<p class="abs lead" style="top:1691px">We believe skincare should restore, not overwhelm.<br>Dew Harbor is built on the idea that fewer, better<br>products — crafted with care and grounded in integrity<br>— can align your skin and spirit.</p>
<div class="abs btn" style="left:512px;top:1944px;width:176px;height:49px">LEARN MORE</div>

<div class="abs tile" style="left:0;width:595px;background:radial-gradient(ellipse at 40% 45%,#e8d0bb 0%,var(--formula) 60%,#c39a78 100%)" role="img" aria-label="Drop of clear serum falling from a glass dropper onto a beige surface">
  <div class="abs tile-label">The<br>Formula</div>
</div>
<div class="abs tile" style="left:607px;width:593px;background:radial-gradient(ellipse at 60% 45%,#dfe3d8 0%,#a9bd9f 40%,var(--tools) 100%)" role="img" aria-label="Jade facial roller and gua sha stone on a white pedestal">
  <div class="abs tile-label">The<br>Tools</div>
</div>

<h2 class="abs h2" style="top:2832px">Every Ingredient Has<br>Purpose</h2>

<div class="abs feature" style="left:73px">
  <svg viewBox="0 0 80 80"><path d="M40 70S10 52 10 30a15 15 0 0 1 30-5 15 15 0 0 1 30 5c0 22-30 40-30 40z"/></svg>
  <span>Cruelty-Free</span>
</div>
<div class="abs feature" style="left:345px">
  <svg viewBox="0 0 80 80"><path d="M50 8l12 8M56 12L30 62a7 7 0 0 1-12-6L44 6"/><path d="M34 40l10 5"/></svg>
  <span>Dermatologist-Tested</span>
</div>
<div class="abs feature" style="left:589px">
  <svg viewBox="0 0 80 80"><path d="M40 8C42 30 50 38 72 40 50 42 42 50 40 72 38 50 30 42 8 40 30 38 38 30 40 8z"/></svg>
  <span>Clean</span>
</div>
<div class="abs feature" style="left:809px">
  <svg viewBox="0 0 80 80"><circle cx="40" cy="40" r="30"/><ellipse cx="40" cy="40" rx="13" ry="30"/><path d="M10 40h60M15 25h50M15 55h50"/></svg>
  <span>Earth-Conscious</span>
</div>

<p class="abs lead" style="top:3193px">We choose ingredients as intentionally as we choose<br>our values — with clarity, purity, and care.</p>
<div class="abs btn" style="left:512px;top:3325px;width:176px;height:48px">LEARN MORE</div>

<h2 class="abs h2" style="top:3504px;font-size:48px;line-height:56px">@dewharbor</h2>

<div class="abs strip" style="left:0;width:229px;background:linear-gradient(160deg,#6b4c3a,#c9977a)" role="img" aria-label="Smiling woman with bare shoulders"></div>
<div class="abs strip" style="left:242px;width:231px;background:linear-gradient(160deg,#e6c49c,#c8956a)" role="img" aria-label="Serum dropped onto the back of a hand"></div>
<div class="abs strip" style="left:486px;width:229px;background:linear-gradient(160deg,#3e2a22,#b27c5c)" role="img" aria-label="Laughing woman applying a dropper to her cheek"></div>
<div class="abs strip" style="left:729px;width:230px;background:linear-gradient(160deg,#c49a80,#e3c3ad)" role="img" aria-label="Close view of freckled skin with a dropper"></div>
<div class="abs strip" style="left:973px;width:227px;background:linear-gradient(160deg,#cfc7c1,#d8a98a)" role="img" aria-label="Smiling older woman with silver hair using a serum dropper"></div>

<footer class="abs footer"></footer>
<div class="abs flinks" style="left:5px;top:4052px">Home<br>Our Story<br>Shop<br>Product Details<br>Rewards<br>FAQs<br>Contact</div>
<div class="abs fbrand">DEW HARBOR</div>
<div class="abs signup" style="top:4121px;font-size:15px;font-weight:700">Let's Stay Aligned</div>
<div class="abs signup" style="top:4153px;font-size:13.5px;line-height:22px;color:var(--ink-soft)">Be the first to know about launches, journal entries, and limited offers.</div>
<div class="abs email"><span>Email Address</span><span>OK</span></div>
<div class="abs flinks" style="left:866px;top:4052px">Account/Subscription<br>Shipping<br>Return Policy<br>Privacy Policy<br>Terms &amp; Conditions<br>Accessibility Statement</div>
<div class="abs copy">2025 Dew Harbor. All Rights Reserved.</div>

</body>
</html>
```